Wine Label Design for Marrick Estate

I need a front and back label for a new wine I am making. I am looking for a classic, elegant and serious wine label. I would like the label to be white with blue and black writing. The blue will be the distinction in the label. The color of blue will be unique and catch the eye. The font of the writing will be unique and could also serve as the brand image for Marrick Estate. The label can have a design but should be simple and distinct. I envision the paper quality of the label to textured, high quality and add to the overall image of the label.
The label will be timeless. The price of this wine will be $85.00 a bottle, and the label should match a higher priced wine. This wine is family owned and operated.
The writing on the front and back label will be:

FRONT Label-

Marrick Estate

Howell Mountain

Napa Valley

2022 Cabernet Sauvignon

Back Label-

Cellared and Bottled by Marrick Estate, Angwin, CA 94508

GOVERNMENT WARNING: (1) According to the Surgeon General, women should not drink alcoholic beverages during pregnancy because of the risk of birth defects. (2) Consumption of alcoholic beverages impairs your ability to drive a car or operate machinery, and may cause health problems.

Alc. 14.5% by Vol.

750 ml

Contains Sulfites

```html
<!DOCTYPE html>
<html lang="en">
<head>
<meta charset="utf-8">
<title>Marrick Estate – Front Label</title>
<link rel="stylesheet" href="https://fonts.googleapis.com/css2?family=Zilla+Slab:wght@300;500&family=Montserrat:wght@500&family=Berkshire+Swash&display=swap">
<style>
  :root {
    --backdrop: #0b0b0b;
    --paper: #f6f6f4;
    --paper-shade: #ecece9;
    --estate-blue: #1f4f9c;
    --ink: #161616;
  }
  html, body {
    margin: 0;
    padding: 0;
    width: 1200px;
    height: 2847px;
    overflow: hidden;
    background: var(--backdrop);
  }
  .canvas {
    position: relative;
    width: 1200px;
    height: 2847px;
  }
  .front-label {
    position: absolute;
    left: 100px;
    top: 761px;
    width: 1000px;
    height: 1325px;
    background:
      repeating-linear-gradient(0deg, rgba(0,0,0,0.012) 0 2px, transparent 2px 5px),
      repeating-linear-gradient(90deg, rgba(0,0,0,0.012) 0 2px, transparent 2px 6px),
      linear-gradient(180deg, var(--paper) 0%, var(--paper-shade) 100%);
    text-align: center;
  }
  .ornament {
    position: absolute;
    left: 380px;
    top: 74px;
    width: 225px;
    height: 44px;
    display: block;
  }
  .estate-name {
    position: absolute;
    left: 0;
    right: 0;
    top: 228px;
    margin: 0;
    font-family: "Zilla Slab", Georgia, serif;
    font-weight: 500;
    font-size: 104px;
    line-height: 120px;
    letter-spacing: 4px;
    text-transform: uppercase;
    color: var(--estate-blue);
  }
  .sub-appellation {
    position: absolute;
    left: 0;
    right: 0;
    top: 617px;
    margin: 0;
    font-family: "Montserrat", Arial, sans-serif;
    font-weight: 500;
    font-size: 50px;
    line-height: 60px;
    letter-spacing: 1px;
    color: var(--ink);
  }
  .region {
    position: absolute;
    left: 0;
    right: 0;
    top: 830px;
    margin: 0;
    font-family: "Berkshire Swash", "Times New Roman", serif;
    font-size: 70px;
    line-height: 84px;
    letter-spacing: 3px;
    color: var(--estate-blue);
  }
  .vintage {
    position: absolute;
    left: 0;
    right: 0;
    top: 1058px;
    margin: 0;
    font-family: "Zilla Slab", Georgia, serif;
    font-weight: 300;
    font-size: 66px;
    line-height: 76px;
    color: var(--estate-blue);
  }
  .varietal {
    position: absolute;
    left: 0;
    right: 0;
    top: 1142px;
    margin: 0;
    font-family: "Zilla Slab", Georgia, serif;
    font-weight: 300;
    font-size: 84px;
    line-height: 96px;
    letter-spacing: 1px;
    color: var(--ink);
  }
</style>
</head>
<body>
  <div class="canvas">
    <section class="front-label">
      <svg class="ornament" viewBox="0 0 225 44" role="img" aria-label="Small blue flourish ornament">
        <rect x="0" y="0" width="225" height="44" rx="22" fill="var(--estate-blue)" opacity="0.35"/>
      </svg>
      <h1 class="estate-name">Marrick<br>Estate</h1>
      <p class="sub-appellation">Howell Mountain</p>
      <p class="region">Napa Valley</p>
      <p class="vintage">2022</p>
      <p class="varietal">Cabernet Sauvignon</p>
    </section>
  </div>
</body>
</html>
```